Business Card Design for Fashion Tech Startup

Dear designers, we need a business card for Asia's premier fashion tech startup.!

PebbleHop is discovery e-commerce destination for busy, discerning parents in Asia featuring leading independent designers of baby, kids fashion apparel and sustainable brands from around the world.

PebbleHop is a modern, contemporary fashion tech startup targeting well-educated, well travelled and affluent parents. We're NOT your typical kiddy store!! Our design philosophy & e-commerce site is more like Vask.com, Orimesa.com, Pondwick.com, Farthollow.com.
Updates

Hi, size of the business card should be 84mm X 55mm. Would appreciate some business card layouts in Portrait as added consideration, i fancy the idea of a Portrait business card. What's important is that the business card should pique the receiver's interest to log onto the website to learn more. Many thanks and love forward to the designs!

Target Market(s)

Though modern, classy in look, feel & positioning, PebbleHop does possess a cheeky, fun-loving personality as depicted by its logo and the segment it targets (baby, kids) though the key decision makers i.e primarily mums between 25-40 who are well educated/travelled, local & expatriates, internet/digitally savvy, mid-high income working mums.

Industry/Entity Type

E-Commerce

Requirements
Must have
• Name, designation, email, phone & mobile number.
Company url : www.pebblehop.sg
Slogan : Discovery e-commerce destination for discerning, busy parents
Nice to have
• Call to Action such as a Discount code offering 10% discount
or asking people to "Like" us on our Chatterly page/Chatterly URL

```html
<!DOCTYPE html>
<html lang="en">
<head>
<meta charset="utf-8">
<title>PebbleHop business card</title>
<link rel="stylesheet" href="https://fonts.googleapis.com/css2?family=Lobster+Two:ital,wght@0,700;1,400;1,700&family=Yesteryear&family=Cormorant+Garamond:wght@500&family=Special+Elite&display=swap">
<style>
  :root {
    --backdrop: #ece7df;
    --card: #fdfaf0;
    --slate: #3d5a6c;
    --coral: #f07f6b;
  }
  * { margin: 0; padding: 0; box-sizing: border-box; }
  html, body { width: 1200px; height: 771px; overflow: hidden; }
  body { background: var(--backdrop); position: relative; }

  .card {
    position: absolute; top: 106px; width: 364px; height: 555px;
    background: var(--card);
    box-shadow: 0 2px 8px rgba(0,0,0,.18);
  }
  .card--front { left: 206px; }
  .card--back { left: 626px; }
  .card-frame { position: absolute; inset: 0; }
  .card-frame line, .card-frame rect { stroke: var(--slate); fill: none; }

  .centered { position: absolute; left: 0; width: 100%; text-align: center; }

  .brand-mark {
    top: 128px; display: flex; justify-content: center; align-items: center; gap: 10px;
    font-family: "Lobster Two", cursive; font-weight: 700; font-size: 30px; color: var(--slate);
  }
  .brand-dot { width: 16px; height: 16px; border-radius: 50%; background: var(--coral); }

  .person-name { top: 310px; font-family: "Yesteryear", cursive; font-size: 38px; color: var(--slate); line-height: 1; }
  .person-role { top: 358px; font-family: "Cormorant Garamond", serif; font-size: 16px; letter-spacing: 3px; color: var(--slate); }

  .rule { position: absolute; left: 40px; width: 284px; border-top: 2px solid var(--slate); }
  .rule::after { content: ""; position: absolute; left: 0; right: 0; top: 2px; border-top: 1px solid var(--slate); }

  .contact-list { position: absolute; left: 60px; top: 440px; list-style: none; }
  .contact-list li {
    display: flex; align-items: center; gap: 8px; height: 32px;
    font-family: "Lobster Two", cursive; font-style: italic; font-size: 26px; color: var(--coral);
  }
  .contact-list svg { fill: var(--coral); }

  .slogan {
    top: 100px; padding: 0 30px;
    font-family: "Lobster Two", cursive; font-style: italic; font-weight: 700;
    font-size: 23px; line-height: 37px; color: var(--slate);
  }
  .offer { top: 272px; font-family: "Special Elite", cursive; font-size: 27px; letter-spacing: 1px; color: var(--coral); }
  .site-url { top: 370px; font-family: "Lobster Two", cursive; font-style: italic; font-weight: 700; font-size: 24px; color: var(--slate); }
  .site-email { top: 404px; font-family: "Lobster Two", cursive; font-style: italic; font-size: 18px; color: var(--slate); }
  .site-social {
    top: 430px; display: flex; justify-content: center; align-items: center; gap: 6px;
    font-family: "Lobster Two", cursive; font-style: italic; font-weight: 700; font-size: 18px; color: var(--slate);
  }
  .social-square { width: 14px; height: 14px; background: var(--slate); }
</style>
</head>
<body>

<section class="card card--front">
  <svg class="card-frame" viewBox="0 0 364 555" aria-hidden="true">
    <line x1="38" y1="16" x2="326" y2="16" stroke-width="1"/>
    <line x1="34" y1="21" x2="330" y2="21" stroke-width="2"/>
    <line x1="38" y1="539" x2="326" y2="539" stroke-width="1"/>
    <line x1="34" y1="534" x2="330" y2="534" stroke-width="2"/>
    <rect x="16" y="30" width="332" height="495" stroke-width="1.5"/>
    <rect x="24" y="38" width="316" height="479" stroke-width="1"/>
  </svg>

  <div class="centered brand-mark"><span class="brand-dot"></span><span>PebbleHop.sg</span></div>

  <h1 class="centered person-name">Mara Quill</h1>
  <p class="centered person-role">manager</p>

  <div class="rule" style="top:428px"></div>
  <ul class="contact-list">
    <li>
      <svg width="22" height="18" viewBox="0 0 22 18" aria-label="phone"><path d="M2 6c0-3 4-5 9-5s9 2 9 5v2h-5V6H7v2H2z"/><rect x="4" y="9" width="14" height="8" rx="1"/></svg>
      +1555 014 227
    </li>
    <li>
      <svg width="22" height="24" viewBox="0 0 22 24" aria-label="mobile"><rect x="6" y="1" width="11" height="22" rx="2"/><rect x="8" y="4" width="7" height="7" fill="#fdfaf0"/></svg>
      +155 5014 0392
    </li>
  </ul>
</section>

<section class="card card--back">
  <svg class="card-frame" viewBox="0 0 364 555" aria-hidden="true">
    <line x1="38" y1="16" x2="326" y2="16" stroke-width="1"/>
    <line x1="34" y1="21" x2="330" y2="21" stroke-width="2"/>
    <line x1="38" y1="539" x2="326" y2="539" stroke-width="1"/>
    <line x1="34" y1="534" x2="330" y2="534" stroke-width="2"/>
    <rect x="16" y="30" width="332" height="495" stroke-width="1.5"/>
    <rect x="24" y="38" width="316" height="479" stroke-width="1"/>
  </svg>

  <div class="rule" style="top:84px"></div>
  <p class="centered slogan">Discovery e-commerce destination for discerning, busy parents</p>
  <div class="rule" style="top:254px"></div>
  <p class="centered offer">10% DISCOUNT!!!</p>
  <div class="rule" style="top:318px"></div>

  <p class="centered site-url">www.pebblehop.sg</p>
  <p class="centered site-email">info@pebblehop.com</p>
  <p class="centered site-social"><span>chatterly.com.pebblehop</span><span class="social-square"></span></p>
  <div class="rule" style="top:462px"></div>
</section>

</body>
</html>
```